KVB WordPress Design Project

• Current web site is www.MossgateArchive.example
• Design client rejected is http://198.51.100.47/~kvb/
• Need Home Page design
o Would like 4 sections in the body of the page to describe key services and link to pages
• Prefers gray or black background. So font would need to be white or light and probably bold to make it easier to read.
• Sites the client really likes
o Zkt.example
o Velmarind-usa.example (Likes 3 sections. Likes black navigation bar.)
• Sites the client doesn’t like
o Tobrick.example
o Qlvzine.example
o Sites that scream “This is a WordPress site!”
• Logo – Client is getting a transparent background logo with white lettering. It’s OK to use current logo for the design.
Updates

Great options!  I have emailed the designs to my client for review.  Will have feedback for you asap.

The client has postponed the decision until Thursday. They have a big event tomorrow that is distracting them.  I'll get back to you asap!

Thank you all for very excellent designs. The client has made a choice. This was my first PixelHarbor project. It worked so well that I will be back!

Target Market(s)

architects, general contractors, interior designers

Requirements
Must have
• PSD files of final design.

Top navigation

Medium gray or dark background.

4 sections on Home Page to describe top 4 services and link to those pages of site. Sections need to be clearly distinguished like the boxes on velmarind-usa. Can't be 4 sections on solid gray background. Sections need to "pop."
Nice to have

Should not have
• Design must go across the page. No sides like the design at
http://198.51.100.47/~kvb

```html
<!DOCTYPE html>
<html lang="en">
<head>
<meta charset="utf-8">
<title>Mossgate Archive — Home</title>
<link href="https://fonts.googleapis.com/css2?family=PT+Sans:wght@400;700&family=PT+Sans+Narrow:wght@400;700&family=Source+Sans+3:wght@300;400&display=swap" rel="stylesheet">
<style>
:root{
  --ink:#1d1d1d;
  --brand-red:#e5242a;
  --card-head:#000000;
  --card-body:#2b2b2b;
  --card-text:#e6e6e6;
  --button:#e8261f;
  --muted:#555555;
  --rule:#d6d6d6;
  --footer-bg:#f4f4f4;
  --photo-dark:#3a3328;
  --photo-warm:#a0672e;
}
*{box-sizing:border-box;margin:0;padding:0}
html,body{width:948px;height:1200px;overflow:hidden;background:#fff}
body{position:relative;font-family:"Source Sans 3",sans-serif;color:var(--ink)}

.site-header{position:absolute;left:0;top:0;width:948px;height:117px}
.brand{position:absolute;left:41px;top:44px;display:flex;align-items:center;gap:10px}
.brand-mark{width:22px;height:22px;background:var(--brand-red)}
.brand-name{font-family:"PT Sans",sans-serif;font-size:27px;font-weight:400;letter-spacing:1px;color:var(--ink)}
.main-nav{position:absolute;right:55px;top:66px;display:flex}
.main-nav a{font-family:"PT Sans",sans-serif;font-size:15px;color:var(--ink);text-decoration:none;padding:0 15px;border-left:1px solid var(--rule);line-height:20px}
.main-nav a:first-child{border-left:none}
.main-nav a:last-child{padding-right:0}

.hero{position:absolute;left:0;top:117px;width:948px;height:446px;
  background:radial-gradient(ellipse at 50% 55%,var(--photo-warm) 0%,#6b4a28 35%,var(--photo-dark) 75%,#1f1c17 100%)}
.hero-dots{position:absolute;left:447px;top:511px;display:flex;gap:4px}
.hero-dots span{width:8px;height:8px;border-radius:50%;background:#fff}

.service{position:absolute;width:404px;height:161px;background:var(--card-body);
  clip-path:polygon(0 0,100% 0,100% calc(100% - 34px),calc(100% - 35px) 100%,0 100%)}
.service-shadow{position:absolute;width:380px;height:8px;border-radius:50%;
  background:radial-gradient(ellipse,rgba(0,0,0,.18),rgba(0,0,0,0) 70%)}
.service h2{height:45px;background:var(--card-head);color:#fff;font-family:"PT Sans",sans-serif;font-weight:400;font-size:21px;padding:12px 0 0 29px;line-height:24px}
.service p{color:var(--card-text);font-size:12px;font-weight:300;line-height:17.3px;padding:8px 36px 0 31px}
.service .cta{position:absolute;left:28px;top:118px;width:124px;height:23px;background:var(--button);border-radius:3px;color:#fff;font-family:"PT Sans Narrow",sans-serif;font-weight:700;font-size:11px;line-height:23px;text-align:center;text-decoration:none}

.news-title{position:absolute;left:54px;top:931px;font-family:"PT Sans Narrow",sans-serif;font-weight:700;font-size:20px;color:#222}
.news-item{position:absolute;top:963px;width:270px}
.news-item h3{font-family:"PT Sans",sans-serif;font-weight:400;font-size:14px;color:#222;margin-bottom:6px}
.news-item p{font-size:11.5px;font-weight:300;line-height:17.3px;color:#333;height:55px}
.news-item .more{display:inline-block;margin-top:5px;font-size:11.5px;color:#222;text-decoration:none}
.news-item .more svg{margin-left:3px;vertical-align:0}
.news-divider{position:absolute;top:966px;width:1px;height:101px;background:var(--rule)}

.site-footer{position:absolute;left:0;top:1123px;width:948px;height:77px;background:var(--footer-bg)}
.copyright{position:absolute;left:61px;top:21px;font-size:11.5px;font-weight:300;color:var(--muted)}
.social{position:absolute;right:29px;top:20px;display:flex;gap:4px}
.social span{width:19px;height:19px;border-radius:2px;background:#3d78c2}
</style>
</head>
<body>
<header class="site-header">
  <div class="brand"><span class="brand-mark"></span><span class="brand-name">MOSSGATE ARCHIVE</span></div>
  <nav class="main-nav">
    <a href="#">HOME</a><a href="#">ASSOCIATIONS</a><a href="#">PRODUCTS</a><a href="#">CALENDER</a><a href="#">CONTACT</a>
  </nav>
</header>

<div class="hero" role="img" aria-label="Photo of a two-level library reading room with wooden bookshelves, railings and a long table"></div>
<div class="hero-dots"><span></span><span></span><span></span><span></span></div>

<div class="service-shadow" style="left:65px;top:695px"></div>
<section class="service" style="left:53px;top:534px">
  <h2>BINDER FINDER</h2>
  <p>Duis tincidunt lectus quis dui viverra vestibulum. Suspendisse vulpu-tate aliquam dui. Nulla elementum dui ut augue. Aliquam vehicula mi at mauris. Maecenas placerat, nisl at</p>
  <a class="cta" href="#">CLICK HERE TO PROCEED</a>
</section>

<div class="service-shadow" style="left:499px;top:695px"></div>
<section class="service" style="left:487px;top:534px">
  <h2>BOX LUNCH BUREAU</h2>
  <p>Duis tincidunt lectus quis dui viverra vestibulum. Suspendisse vulpu-tate aliquam dui. Nulla elementum dui ut augue. Aliquam vehicula mi at mauris. Maecenas placerat, nisl at</p>
  <a class="cta" href="#">CLICK HERE TO PROCEED</a>
</section>

<div class="service-shadow" style="left:65px;top:894px"></div>
<section class="service" style="left:53px;top:733px">
  <h2>DONUTS &amp; A DEMO</h2>
  <p>Duis tincidunt lectus quis dui viverra vestibulum. Suspendisse vulpu-tate aliquam dui. Nulla elementum dui ut augue. Aliquam vehicula mi at mauris. Maecenas placerat, nisl at</p>
  <a class="cta" href="#">CLICK HERE TO PROCEED</a>
</section>

<div class="service-shadow" style="left:499px;top:894px"></div>
<section class="service" style="left:487px;top:733px">
  <h2>COOKIES &amp; QUESTIONS</h2>
  <p>Duis tincidunt lectus quis dui viverra vestibulum. Suspendisse vulpu-tate aliquam dui. Nulla elementum dui ut augue. Aliquam vehicula mi at mauris. Maecenas placerat, nisl at</p>
  <a class="cta" href="#">CLICK HERE TO PROCEED</a>
</section>

<h2 class="news-title">RECENT NEWS</h2>

<article class="news-item" style="left:55px">
  <h3>Suspendisse quam leo</h3>
  <p>The Mossgate Archive Tradeshow in conjunction with the NDA Regional Conference<br>Download3</p>
  <a class="more" href="#">Learn more<svg width="4" height="7" viewBox="0 0 4 7"><path d="M0 0L4 3.5L0 7Z" fill="#999"/></svg></a>
</article>
<div class="news-divider" style="left:338px"></div>
<article class="news-item" style="left:358px">
  <h3>Morbi eget arcu</h3>
  <p>Morbi porta, libero id ullamcorper nonummy, nibh ligula pulvinar metus, eget consectetuer augue nisi quis lacus.</p>
  <a class="more" href="#">Learn more<svg width="4" height="7" viewBox="0 0 4 7"><path d="M0 0L4 3.5L0 7Z" fill="#999"/></svg></a>
</article>
<div class="news-divider" style="left:625px"></div>
<article class="news-item" style="left:647px">
  <h3>Cum sociis natoque</h3>
  <p>Eastern Ridge Area Conference/TradeShow in Harlow, Sablewood Canyon Resort, more details call 555-014-2290. This takes the place ..</p>
  <a class="more" href="#">Learn more<svg width="4" height="7" viewBox="0 0 4 7"><path d="M0 0L4 3.5L0 7Z" fill="#999"/></svg></a>
</article>

<footer class="site-footer">
  <p class="copyright">© 2012 Company Name.&nbsp; All right reserved.&nbsp; Term of Use</p>
  <div class="social" aria-label="Social links"><span></span><span></span><span></span><span></span></div>
</footer>
</body>
</html>
```